Website design for an Online pastry shop

Website Name : www.lanternandplum.example

Description of the website and its target audience
We are a premium pastry company producing delicious cakes, macarons, cookies, gelato, and other sweet dessert. Our differentiation is that our products are freshly produced with premium quality imported ingredients and one bite into our products set us apart from other bakery shop. We online retail online so as to provide high quality products at a affordable cost. Our products has received raving reviews by many food enthusiast even the hard to please ones. The products contain more natural ingredients and we do not add preservatives. The return rates for our pastry is almost 80%. You only need to try once to be return customers. Our greatest challenge is getting customer to take the first bite. We are so sure of our products that we are going to give people free food tasting.

We are based in China but all our products are developed by award winning chefs from 5 stars hotel. The target customer is woman 16 to 40+ in china. Working class ladies and demand high quality products. A modern, sophisticated and minimalist website

This is a competitive market and image is crucial for such a food ‘conscious ’ orientated customer. They want to feel that they are buying from a reliable company that take great effort to ensure food cleaniness and safety yet affordable price. We make almost 98% of sub ingredients ourselves and we make it by hand.

Style/theme ideas for the web page design
I am looking for a elegant a little rustic, handmade feel yet sophisticated design - one that is easy to the eye yet functional and easy for the user to navigate through. Good play of fonts to give let it feel unique and customised. Black and white is our corporate colours. However, we do not want black background as it does not tease the taste bud. All our colours should come from our products. Customers should be very close to our products. They eat with their eyes first. Black and white is just accent.

Inspirational and competitors websites
http://www.47tart.example/ ( Key competitor )
I like the simple, clean look. The products are the key focus
https://www.pelvora.example/
clean, fresh and different. Attractive with purpose. Feminine
http://moatandwillow.example/
this has a great layout - lots of information and nicely presented. Very sweet and feminine
http://www.storeharbourly.example/
product features is the focus
http://www.janetobrill.example/store/
fun, feminine, rustic

Number of pages needed : 6 ( Uncoded PSD design only )
Page descriptions
Home Page - This page will show what makes our products stand out from the competitors and provide an introduction of who we are.
2nd page : Product catalogue
3nd page: Detail Product page with pictures and descriptions. Select products size and add to cart....
4rd page: Brand Story with pictures and descriptions.
5th page Contact Us : Here they can contact or schedule an appointment for free product tasting
6th page : Check out page

• Please see the project wire frame file " main page.png " or file number 70

```html
<!DOCTYPE html>
<html lang="en">
<head>
<meta charset="utf-8">
<title>Lantern &amp; Plum — Premium Pastry</title>
<link rel="stylesheet" href="https://fonts.googleapis.com/css2?family=Marcellus&family=Alegreya:ital@0;1&family=Open+Sans:wght@400;600&display=swap">
<style>
:root{
  --ink:#2b2b2b;
  --bar:#262626;
  --footer:#1e1e1e;
  --news:#4a4548;
  --accent:#e8262c;
  --muted:#8a8585;
  --body:#4a3f3a;
  --tag:#ecd6c3;
  --quote:#ddd6dc;
  --white:#ffffff;
  --line:#e4e0e0;
}
*{margin:0;padding:0;box-sizing:border-box}
html,body{width:1200px;height:2177px;overflow:hidden;background:var(--white)}
body{position:relative;font-family:"Open Sans",Arial,sans-serif;color:var(--ink)}
.abs{position:absolute}

/* top bar */
.topbar{left:0;top:0;width:1200px;height:97px;background:var(--bar)}
.delivery-badge{left:87px;top:31px;width:235px;height:32px;background:var(--accent);color:var(--white);font-size:14px;line-height:32px;text-align:center}
.brand{left:450px;top:12px;width:300px;text-align:center;color:var(--white)}
.brand-dot{display:block;width:30px;height:30px;border:2px solid var(--white);border-radius:50%;margin:0 auto 10px}
.brand-name{font-family:"Marcellus",Georgia,serif;font-size:17px;letter-spacing:.5px}
.account-links{right:87px;top:34px;color:var(--white);font-size:13px}
.account-links span{margin:0 9px}

/* main nav */
.main-nav{left:0;top:97px;width:1200px;height:41px;border-bottom:1px solid var(--line);display:flex;justify-content:center;gap:0}
.main-nav a{position:absolute;top:12px;font-family:"Marcellus",Georgia,serif;font-size:16px;color:var(--ink);text-decoration:none;letter-spacing:.5px}

/* hero */
.hero{left:0;top:138px;width:1200px;height:452px;background:
  radial-gradient(ellipse 340px 230px at 760px 230px,#f4efe6 0%,#f1e7dc 55%,transparent 80%),
  radial-gradient(circle 60px at 150px 330px,#9fd3c0 0%,transparent 100%),
  radial-gradient(circle 70px at 280px 210px,#e98d93 0%,transparent 100%),
  radial-gradient(circle 80px at 800px 400px,#d83a45 0%,transparent 100%),
  linear-gradient(180deg,#e9d7c8 0%,#c48a5c 55%,#8e5a35 100%)}
.hero-card{left:578px;top:290px;width:535px;height:170px;background:rgba(40,36,34,.72);color:var(--white);padding:20px 36px}
.hero-kicker{font-family:"Marcellus",Georgia,serif;font-size:22px;letter-spacing:1px}
.hero-title{font-family:"Marcellus",Georgia,serif;font-size:30px;letter-spacing:1px;margin-top:2px}
.hero-text{font-size:14px;line-height:22px;margin-top:8px}

/* welcome */
.section-title{font-family:"Marcellus",Georgia,serif;font-size:36px;color:var(--ink);letter-spacing:1px}
.section-sub{font-family:"Marcellus",Georgia,serif;font-size:18px;color:var(--muted)}
.welcome-photo{left:87px;top:714px;width:281px;height:218px;background:linear-gradient(180deg,#3a2219 0%,#6e4130 40%,#e9dcc8 55%,#5a3324 75%,#f6f2ee 100%)}
.welcome-copy{left:411px;top:734px;width:707px;font-family:"Alegreya",Georgia,serif;font-style:italic;font-size:15.5px;line-height:25px;color:var(--body)}
.welcome-copy p+p{margin-top:22px}
.read-more-link{left:411px;top:940px;font-family:"Alegreya",Georgia,serif;font-style:italic;font-size:14px;color:var(--accent);font-weight:700}

/* products */
.product{width:237px;height:215px}
.product-tag{position:absolute;left:170px;top:24px;width:160px;height:87px;background:var(--tag);font-size:11.5px;line-height:19px;text-align:center;color:var(--ink);padding:9px 8px}

/* quote band */
.quote-band{left:0;top:1595px;width:1200px;height:298px;background:radial-gradient(ellipse 500px 220px at 600px 150px,#efe9ee 0%,var(--quote) 70%,#cfc6cd 100%)}
.quote-lead{left:120px;top:1644px;width:960px;text-align:center;font-family:"Marcellus",Georgia,serif;font-size:25px;line-height:38px;color:#3a3535}
.quote-copy{left:230px;top:1728px;width:740px;text-align:center;font-family:"Alegreya",Georgia,serif;font-style:italic;font-size:14px;line-height:22px;color:#4a4545}
.btn-red{background:var(--accent);color:var(--white);text-align:center;font-family:"Marcellus",Georgia,serif;font-size:14px}
.quote-btn{left:537px;top:1786px;width:126px;height:32px;line-height:32px}

/* newsletter */
.newsletter{left:0;top:1893px;width:1200px;height:120px;background:var(--news)}
.news-title{left:87px;top:1938px;font-family:"Marcellus",Georgia,serif;font-size:23px;color:var(--white)}
.news-input{left:397px;top:1934px;width:368px;height:36px;background:var(--white);font-size:13px;color:#999;line-height:36px;padding-left:14px}
.news-btn{left:784px;top:1934px;width:126px;height:36px;line-height:36px}
.social{top:1936px;width:32px;height:32px;border-radius:50%;background:#c9c6c7}

/* footer */
.site-footer{left:0;top:2013px;width:1200px;height:164px;background:var(--footer)}
.footer-links{left:90px;top:2035px;font-family:"Marcellus",Georgia,serif;font-size:14px;color:var(--white)}
.footer-links span{margin-right:36px}
.footer-contact{left:87px;top:2070px;font-size:13px;line-height:27px;color:var(--white)}
.copyright{left:90px;top:2130px;font-size:11.5px;color:#8d8d8d}
.footer-brand{left:960px;top:2040px;width:210px;text-align:center;color:var(--white)}
</style>
</head>
<body>

<header>
  <div class="abs topbar"></div>
  <div class="abs delivery-badge">Free Delivery For Order Above $50</div>
  <div class="abs brand"><span class="brand-dot"></span><span class="brand-name">Lantern &amp; Plum</span></div>
  <div class="abs account-links">Home<span>|</span>Login<span>|</span>Signup<span>|</span>Cart</div>
  <nav class="abs main-nav">
    <a style="left:262px">CAKES</a>
    <a style="left:348px">MACARONS</a>
    <a style="left:477px">COOKIES</a>
    <a style="left:588px">GELATO</a>
    <a style="left:694px">TASTING ROOM</a>
    <a style="left:858px">ABOUT US</a>
  </nav>
</header>

<section>
  <div class="abs hero" role="img" aria-label="Photo of a giant macaron filled with gelato scoops beside pastel macarons on a wooden board"></div>
  <div class="abs hero-card">
    <div class="hero-kicker">LOREM IPSUM DOLOR</div>
    <div class="hero-title">CONSEC TETUR ADIPISICIN</div>
    <div class="hero-text">Lorem ipsum dolor sit amet, consectetur adipisicing elit, sed do eiusmod tempor incididunt ut labore et dolore magna</div>
  </div>
</section>

<section>
  <h1 class="abs section-title" style="left:87px;top:620px">WELCOME</h1>
  <p class="abs section-sub" style="left:87px;top:663px">Sed ut perspiciatis unde omnis iste natus error sit voluptatem accusantium</p>
  <div class="abs welcome-photo" role="img" aria-label="Photo of a layered chocolate cake slice topped with chocolate shavings"></div>
  <div class="abs welcome-copy">
    <p>At vero eos et accusamus et iusto odio dignissimos ducimus qui blanditiis praesentium voluptatum deleniti atque corrupti quos dolores et quas molestias excepturi sint occaecati cupiditate non provident, similique sunt in culpa qui officia deserunt mollitia animi, id est laborum et dolorum fuga. Et harum quidem rerum facilis est et expedita distinctio.</p>
    <p>Nam libero tempore, cum soluta nobis est eligendi optio cumque nihil impedit quo minus id quod maxime placeat facere possimus, omnis voluptas assumenda est, omnis dolor repellendus. Temporibus autem quibusdam et aut officiis debitis aut rerum necessitatibus saepe eveniet</p>
  </div>
  <a class="abs read-more-link">Read More</a>
</section>

<section>
  <h2 class="abs section-title" style="left:87px;top:1015px;font-size:25px">OUR FEATURED PRODUCTS</h2>
  <p class="abs section-sub" style="left:87px;top:1053px">Sed ut perspiciatis unde omnis iste natus error sit voluptatem accusantium</p>

  <div class="abs product" style="left:87px;top:1116px">
    <div class="abs product" style="left:0;top:0;background:linear-gradient(180deg,#3b241a,#6d4331 55%,#e6d4bb 70%,#7a5236)" role="img" aria-label="Photo of a chocolate layer cake slice"></div>
    <div class="product-tag">Nam libero tempore, cum soluta nobis est eligendi cumque nihil impedit quo</div>
  </div>
  <div class="abs product" style="left:438px;top:1116px">
    <div class="abs product" style="left:0;top:0;background:linear-gradient(180deg,#d5b28c,#f4efe6 55%,#a8754a)" role="img" aria-label="Photo of a cream pie with pastry sticks"></div>
    <div class="product-tag">Nam libero tempore, cum soluta nobis est eligendi cumque nihil impedit quo</div>
  </div>
  <div class="abs product" style="left:789px;top:1116px">
    <div class="abs product" style="left:0;top:0;background:linear-gradient(160deg,#e7d8c2,#a8683a 50%,#6b3f22)" role="img" aria-label="Photo of nut cookies with spices"></div>
    <div class="product-tag">Nam libero tempore, cum soluta nobis est eligendi cumque nihil impedit quo</div>
  </div>
  <div class="abs product" style="left:87px;top:1355px">
    <div class="abs product" style="left:0;top:0;background:radial-gradient(circle at 50% 50%,#4a5a55,#1f2a2a 80%)" role="img" aria-label="Photo of colourful macarons on a dark table"></div>
    <div class="product-tag">Nam libero tempore, cum soluta nobis est eligendi cumque nihil impedit quo</div>
  </div>
  <div class="abs product" style="left:438px;top:1355px">
    <div class="abs product" style="left:0;top:0;background:radial-gradient(circle at 55% 50%,#f39a1e,#e0731a 55%,#f3efea 80%)" role="img" aria-label="Photo of an orange fruit tart"></div>
    <div class="product-tag">Nam libero tempore, cum soluta nobis est eligendi cumque nihil impedit quo</div>
  </div>
  <div class="abs product" style="left:789px;top:1355px">
    <div class="abs product" style="left:0;top:0;background:linear-gradient(180deg,#3a4a3f,#2b2b4a 40%,#f1e6c9 65%,#d9c29a)" role="img" aria-label="Photo of a blueberry cheesecake"></div>
    <div class="product-tag">Nam libero tempore, cum soluta nobis est eligendi cumque nihil impedit quo</div>
  </div>
</section>

<section>
  <div class="abs quote-band" role="img" aria-label="Soft faded photo of a cake behind the quote"></div>
  <p class="abs quote-lead">Temporibus autem quibusdam et aut officiis debitis aut rerum necessitatibus saepe eveniet ut et voluptates repudiandae sint et</p>
  <p class="abs quote-copy">Neque porro quisquam est, qui dolorem ipsum quia dolor sit amet, consectetur, adipisci velit, sed quia non numquam eius modi tempora incidunt ut labore et dolore magnam aliquam quaerat voluptatem</p>
  <div class="abs btn-red quote-btn">Read More</div>
</section>

<section>
  <div class="abs newsletter"></div>
  <div class="abs news-title">Join Our Mailing Newsletter</div>
  <div class="abs news-input">Enter Email Here...</div>
  <div class="abs btn-red news-btn">SUBMIT</div>
  <span class="abs social" style="left:964px"></span>
  <span class="abs social" style="left:1002px"></span>
  <span class="abs social" style="left:1040px"></span>
  <span class="abs social" style="left:1078px"></span>
</section>

<footer>
  <div class="abs site-footer"></div>
  <div class="abs footer-links"><span>Cakes</span><span>Macarons</span><span>Cookies</span><span>Gelato</span><span>Tasting Room</span><span>About us</span></div>
  <div class="abs footer-contact">Call Us For enquiry: 5550142867<br>Email Us: hello@lanternandplum.example</div>
  <div class="abs copyright">Copyright © 2015 Ember Quay Studio. All Rights Reserved. Privacy Policy &nbsp;|&nbsp; Site Map</div>
  <div class="abs footer-brand"><span class="brand-dot"></span><span class="brand-name">Lantern &amp; Plum</span></div>
</footer>

</body>
</html>
```